Corvanel Website Homepage

Committed to delivering quality content, quillmarkwords.example is a content providing company. Equipped with resourceful writers with industry experience, we promise to empower our clients with content that is tailor-made to address specific requirements of their target Audience.

We need a website home page and one internal page designed. It is very important that the page be laid out with SEO in mind. We like the idea of using five images as navigation to our services. The five major services we offer are:
• Web Content writing (articles, features, website copy etc)
• Business Content writing (Press release, mailers & flyers, brochure/catalog)
• Personal Content writing (blog, speech writing)
• Hire a writer/editor
• Proof reading and editing services
The sample template (http://demo7.layoutsample.example/wt_48207/index.html) included has five images in the first fold. Designer can choose the right image for each service and lay over the service name on the image. Please do not use flash ( We will use javascripts). We need to have a detailed right side nav as in the template for SEO reasons. There will be some marketing ad- copy below the main images. Followed by a 200 character SEO optimized text defining our services in further detail. Apart from these a designer is free to use his creativity. The name of the site will be http://www.quillmarkwords.example/. This name will need a logo too. Please include it as part of design. Corvanelcorp is the owner of quillmarkwords.example. We already have a logo for Corvanel that is attached here as a separate file.

We have some taglines that need to be incorporated in the home page and other pages.
Please provide link button for Home, About us, Services, Samples, Pricing, Clients, Career, Contact us.

Links can be given on TOP, Sideways and Bottom and in the drop down menu of services etc.

Reason: Hi

We have made our project guaranteed and extended deadline by 5 days so you get more time to complete our project.

Thanks and Regards,

Ravindra Kulkarni
Corvanelcorp

Target Market(s)

Product Marketing Companies - Mostly in US.
Media companies which publish articles on various subjects. Travel and Lifestyle related sites, Educational Websites, Government Websites, Health related websites,

Industry/Entity Type

Marketing

Requirements
Must have
• Color of Homepage should blend with sober mood of the content. Writing Services should get highlighted in such a way that any person serious about the business visiting the site get attracted to read on the details of our content services. Most space should be used for details of writing services and links for our various pages and services. Webpage should be downloaded in lowest possible time.
Nice to have
• We have some idea about the website layouts;-http://www.pagefoundry.example/website-templates/48207.html - layout of information http://www.pagefoundry.example/website-templates/47915.html - for kind of marketing http://demo7.layoutsample.example/wt_48592/index.html - for colors
we attach a word file representing our idea in some way but not limited to it.
Should not have
• Gaudy (aggressive dark) colors. It should not be cluttered. No flash.

```html
<!DOCTYPE html>
<html lang="en">
<head>
<meta charset="utf-8">
<title>Corvanel — Content Writing Services</title>
<link rel="stylesheet" href="https://fonts.googleapis.com/css2?family=Arimo:ital,wght@0,400;0,700;1,400;1,700&family=Didact+Gothic&display=swap">
<style>
  :root {
    --brand-red: #d4202a;
    --nav-top: #d9ebfa;
    --nav-bottom: #8fc0ea;
    --nav-line: #6fa6d8;
    --ink: #2e3a3a;
    --ink-soft: #4a5555;
    --heading-grey: #5a6566;
    --link-blue: #3a86d4;
    --accent-blue: #3c86d8;
    --accent-orange: #f07c16;
    --panel-light: #fbfbea;
    --panel-dark: #dde3cf;
    --green-a: #8ee01e; --green-b: #56bd0c; --green-btn: #6fd016;
    --yellow-a: #fde6a8; --yellow-b: #f4b02c; --yellow-btn: #f8c24a;
    --orange-a: #fb8a22; --orange-b: #e0530a; --orange-btn: #f06a10;
    --teal-a: #3ae3d0; --teal-b: #10b4aa; --teal-btn: #20ccbc;
    --pink-a: #f25ed8; --pink-b: #d21aa6; --pink-btn: #e23ac0;
  }
  * { box-sizing: border-box; margin: 0; padding: 0; }
  html, body { width: 806px; height: 1200px; overflow: hidden; background: #ffffff; }
  body { font-family: "Didact Gothic", "Century Gothic", sans-serif; color: var(--ink); }
  .page { position: relative; width: 806px; height: 1200px; overflow: hidden; background: #ffffff; }

  .brand { position: absolute; left: 44px; top: 16px; display: flex; align-items: center; gap: 12px; }
  .brand-mark { width: 14px; height: 14px; background: var(--brand-red); }
  .brand-name { font-family: "Didact Gothic", sans-serif; font-size: 30px; color: var(--brand-red); letter-spacing: 0.5px; }

  .main-nav { position: absolute; left: 32px; top: 79px; width: 759px; height: 38px;
    background: linear-gradient(var(--nav-top), var(--nav-bottom)); border: 1px solid var(--nav-line); display: flex; }
  .main-nav a { flex: 1; display: flex; align-items: center; justify-content: center;
    font-family: "Arimo", sans-serif; font-size: 13px; color: #ffffff; text-decoration: none;
    text-shadow: 0 1px 2px rgba(40,80,130,0.7); border-right: 1px solid rgba(255,255,255,0.6); }
  .main-nav a:last-child { border-right: none; }

  .hero { position: absolute; left: 32px; top: 117px; width: 759px; height: 279px;
    background: linear-gradient(90deg, #eef1f2 0%, #ffffff 55%, #fafcf4 100%); overflow: hidden; }
  .hero-photo { position: absolute; left: 0; top: 0; width: 330px; height: 279px;
    background: linear-gradient(100deg, #c9ccd0 0%, #d8dbe0 35%, #e7ebef 70%, rgba(245,247,248,0) 100%); }
  .hero-bubble { position: absolute; left: 308px; top: 50px; width: 380px; height: 166px;
    border: 1px solid #dde2e6; border-radius: 10px; background: rgba(255,255,255,0.75);
    box-shadow: 0 2px 6px rgba(0,0,0,0.08); }
  .hero-bubble svg { position: absolute; left: 64px; top: 164px; }
  .hero-title { position: absolute; left: 342px; top: 62px; width: 360px;
    font-family: "Arimo", sans-serif; font-weight: 700; font-size: 17px; color: var(--accent-blue);
    line-height: 23px; text-shadow: 0 1px 1px rgba(0,0,0,0.15); }
  .hero-title span { display: block; }
  .hero-title span + span { text-align: right; }
  .hero-lead { position: absolute; left: 326px; top: 118px; width: 360px;
    font-size: 18.5px; line-height: 24px; color: var(--accent-orange); }

  .services { position: absolute; left: 32px; top: 396px; width: 759px; height: 330px; display: flex; }
  .service { position: relative; flex: 1; border-right: 1px solid rgba(255,255,255,0.5); color: #3a3a1a; }
  .service:last-child { border-right: none; }
  .service-web { background: linear-gradient(var(--green-a), var(--green-b)); }
  .service-business { background: linear-gradient(var(--yellow-a), var(--yellow-b)); }
  .service-personal { background: linear-gradient(var(--orange-a), var(--orange-b)); }
  .service-hire { background: linear-gradient(var(--teal-a), var(--teal-b)); }
  .service-proof { background: linear-gradient(var(--pink-a), var(--pink-b)); }
  .service-title { position: absolute; left: 10px; top: 18px; font-family: "Arimo", sans-serif;
    font-style: italic; font-weight: 700; font-size: 14px; line-height: 18px; color: #ffffff;
    text-transform: uppercase; text-shadow: 0 1px 2px rgba(0,0,0,0.35); }
  .service-list { position: absolute; left: 8px; top: 76px; list-style: none; }
  .service-list li { display: flex; align-items: center; gap: 10px; height: 22px;
    font-family: "Arimo", sans-serif; font-size: 10px; color: #2f3010; }
  .service-list svg { flex: none; }
  .service-copy { position: absolute; left: 8px; top: 206px; width: 138px;
    font-family: "Arimo", sans-serif; font-style: italic; font-size: 10px; line-height: 12.5px; color: #2f3010;
    border-top: 1px solid rgba(255,255,255,0.45); padding-top: 8px; }
  .service-cta { position: absolute; left: 0; right: 0; bottom: 0; height: 49px;
    display: flex; align-items: center; justify-content: flex-end; padding-right: 12px; gap: 5px;
    font-family: "Arimo", sans-serif; font-style: italic; font-weight: 700; font-size: 15px;
    color: #4a4a40; text-decoration: none; border-top: 1px solid rgba(255,255,255,0.7); }
  .service-web .service-cta { background: var(--green-btn); }
  .service-business .service-cta { background: var(--yellow-btn); }
  .service-personal .service-cta { background: var(--orange-btn); }
  .service-hire .service-cta { background: var(--teal-btn); }
  .service-proof .service-cta { background: var(--pink-btn); }
  .service-cta b { color: #ffffff; font-size: 15px; }

  .content { position: absolute; left: 32px; top: 726px; width: 759px; height: 414px;
    background: linear-gradient(var(--panel-light), var(--panel-dark)); display: flex; }
  .news { width: 500px; padding: 28px 0 0 24px; border-right: 1px solid #c9cdbf; }
  .section-title { font-family: "Arimo", sans-serif; font-style: italic; font-weight: 700;
    font-size: 21px; color: var(--heading-grey); letter-spacing: 0.3px; }
  .news-list { list-style: none; margin-top: 18px; }
  .news-item { display: flex; gap: 14px; height: 76px; position: relative; }
  .news-item::after { content: ""; position: absolute; left: 40px; right: 70px; bottom: 16px; height: 1px; background: #dadccc; }
  .news-item:last-child::after { display: none; }
  .news-item p { width: 390px; font-size: 13.5px; line-height: 16px; color: var(--ink); }
  .news-item:nth-child(even) p { color: var(--accent-blue); }

  .quick-links { flex: 1; padding: 28px 0 0 26px; }
  .quick-links .section-title { text-align: center; margin-right: 20px; }
  .quick-links ul { list-style: none; margin-top: 20px; }
  .quick-links li { height: 23.5px; }
  .quick-links a { font-family: "Arimo", sans-serif; font-weight: 700; font-size: 9.5px; color: var(--link-blue); }

  .site-footer { position: absolute; left: 32px; top: 1146px; width: 759px; height: 54px;
    background: linear-gradient(#c9cfcf, #f6f8f6 60%, #ffffff); display: flex; align-items: center;
    justify-content: space-between; padding: 10px 24px 0 26px; font-size: 12px; color: #6a6f70; }
  .footer-links a { color: #6a6f70; }
  .footer-links span { margin: 0 10px; }
</style>
</head>
<body>
<div class="page">

  <header class="brand">
    <span class="brand-mark"></span>
    <span class="brand-name">Corvanel</span>
  </header>

  <nav class="main-nav">
    <a href="#">HOME PAGE</a>
    <a href="#">ABOUT US</a>
    <a href="#">PRODUCTS</a>
    <a href="#">SERVICES</a>
    <a href="#">SUPPORT</a>
    <a href="#">CONTACT US</a>
  </nav>

  <section class="hero">
    <div class="hero-photo" role="img" aria-label="Photo of a smiling businesswoman in front of colleagues meeting at an office table"></div>
    <div class="hero-bubble">
      <svg width="40" height="30" viewBox="0 0 40 30"><path d="M2 0 L10 28 L28 0" fill="rgba(255,255,255,0.75)" stroke="#dde2e6"/></svg>
    </div>
    <h1 class="hero-title"><span>Mauris posuere. Aliquam semper,</span><span>Vivamus nec massa vitae</span></h1>
    <p class="hero-lead">Phasellus condimentum hendrerit elit. Nullam pede magna, sagittis ac, mollis eget, eleifend eget, erat. Mauris</p>
  </section>

  <section class="services">
    <article class="service service-web">
      <h2 class="service-title">Web<br>Content</h2>
      <ul class="service-list">
        <li><svg width="14" height="14"><rect width="14" height="14" fill="#eef0ee"/><path d="M5 3 L10 7 L5 11Z" fill="#9aa0a0"/></svg>Vivamus mollis, massa</li>
        <li><svg width="14" height="14"><rect width="14" height="14" fill="#eef0ee"/><path d="M5 3 L10 7 L5 11Z" fill="#9aa0a0"/></svg>Suspendisse potenti.</li>
        <li><svg width="14" height="14"><rect width="14" height="14" fill="#eef0ee"/><path d="M5 3 L10 7 L5 11Z" fill="#9aa0a0"/></svg>Etiam enim nisl, i</li>
        <li><svg width="14" height="14"><rect width="14" height="14" fill="#eef0ee"/><path d="M5 3 L10 7 L5 11Z" fill="#9aa0a0"/></svg>Praesent commodo</li>
        <li><svg width="14" height="14"><rect width="14" height="14" fill="#eef0ee"/><path d="M5 3 L10 7 L5 11Z" fill="#9aa0a0"/></svg>Nulla auctor laoreet</li>
      </ul>
      <p class="service-copy">Etiam enim nisl, interdum eu, dictum nec, euismod eu, leo. Morbi dictum. Donec tincidunt. Nam viverra. Donec posuere.</p>
      <a class="service-cta" href="#">click here <b>&gt;&gt;</b></a>
    </article>
    <article class="service service-business">
      <h2 class="service-title">Business<br>Content</h2>
      <ul class="service-list">
        <li><svg width="14" height="14"><rect width="14" height="14" fill="#eef0ee"/><path d="M5 3 L10 7 L5 11Z" fill="#9aa0a0"/></svg>Vivamus mollis, massa</li>
        <li><svg width="14" height="14"><rect width="14" height="14" fill="#eef0ee"/><path d="M5 3 L10 7 L5 11Z" fill="#9aa0a0"/></svg>Suspendisse potenti.</li>
        <li><svg width="14" height="14"><rect width="14" height="14" fill="#eef0ee"/><path d="M5 3 L10 7 L5 11Z" fill="#9aa0a0"/></svg>Etiam enim nisl, i</li>
        <li><svg width="14" height="14"><rect width="14" height="14" fill="#eef0ee"/><path d="M5 3 L10 7 L5 11Z" fill="#9aa0a0"/></svg>Praesent commodo</li>
        <li><svg width="14" height="14"><rect width="14" height="14" fill="#eef0ee"/><path d="M5 3 L10 7 L5 11Z" fill="#9aa0a0"/></svg>Nulla auctor laoreet</li>
      </ul>
      <p class="service-copy">Etiam enim nisl, interdum eu, dictum nec, euismod eu, leo. Morbi dictum. Donec tincidunt. Nam viverra. Donec posuere.</p>
      <a class="service-cta" href="#">click here <b>&gt;&gt;</b></a>
    </article>
    <article class="service service-personal">
      <h2 class="service-title">Personal<br>Content</h2>
      <ul class="service-list">
        <li><svg width="14" height="14"><rect width="14" height="14" fill="#eef0ee"/><path d="M5 3 L10 7 L5 11Z" fill="#9aa0a0"/></svg>Vivamus mollis, massa</li>
        <li><svg width="14" height="14"><rect width="14" height="14" fill="#eef0ee"/><path d="M5 3 L10 7 L5 11Z" fill="#9aa0a0"/></svg>Suspendisse potenti.</li>
        <li><svg width="14" height="14"><rect width="14" height="14" fill="#eef0ee"/><path d="M5 3 L10 7 L5 11Z" fill="#9aa0a0"/></svg>Etiam enim nisl, i</li>
        <li><svg width="14" height="14"><rect width="14" height="14" fill="#eef0ee"/><path d="M5 3 L10 7 L5 11Z" fill="#9aa0a0"/></svg>Praesent commodo</li>
        <li><svg width="14" height="14"><rect width="14" height="14" fill="#eef0ee"/><path d="M5 3 L10 7 L5 11Z" fill="#9aa0a0"/></svg>Nulla auctor laoreet</li>
      </ul>
      <p class="service-copy">Etiam enim nisl, interdum eu, dictum nec, euismod eu, leo. Morbi dictum. Donec tincidunt. Nam viverra. Donec posuere.</p>
      <a class="service-cta" href="#">click here <b>&gt;&gt;</b></a>
    </article>
    <article class="service service-hire">
      <h2 class="service-title">Hire a<br>Writer/Editor</h2>
      <ul class="service-list">
        <li><svg width="14" height="14"><rect width="14" height="14" fill="#eef0ee"/><path d="M5 3 L10 7 L5 11Z" fill="#9aa0a0"/></svg>Vivamus mollis, massa</li>
        <li><svg width="14" height="14"><rect width="14" height="14" fill="#eef0ee"/><path d="M5 3 L10 7 L5 11Z" fill="#9aa0a0"/></svg>Suspendisse potenti.</li>
        <li><svg width="14" height="14"><rect width="14" height="14" fill="#eef0ee"/><path d="M5 3 L10 7 L5 11Z" fill="#9aa0a0"/></svg>Etiam enim nisl, i</li>
        <li><svg width="14" height="14"><rect width="14" height="14" fill="#eef0ee"/><path d="M5 3 L10 7 L5 11Z" fill="#9aa0a0"/></svg>Praesent commodo</li>
        <li><svg width="14" height="14"><rect width="14" height="14" fill="#eef0ee"/><path d="M5 3 L10 7 L5 11Z" fill="#9aa0a0"/></svg>Nulla auctor laoreet</li>
      </ul>
      <p class="service-copy">Etiam enim nisl, interdum eu, dictum nec, euismod eu, leo. Morbi dictum. Donec tincidunt. Nam viverra. Donec posuere.</p>
      <a class="service-cta" href="#">click here <b>&gt;&gt;</b></a>
    </article>
    <article class="service service-proof">
      <h2 class="service-title">Proof Reading<br>&amp; Editing Services</h2>
      <ul class="service-list">
        <li><svg width="14" height="14"><rect width="14" height="14" fill="#eef0ee"/><path d="M5 3 L10 7 L5 11Z" fill="#9aa0a0"/></svg>Vivamus mollis, massa</li>
        <li><svg width="14" height="14"><rect width="14" height="14" fill="#eef0ee"/><path d="M5 3 L10 7 L5 11Z" fill="#9aa0a0"/></svg>Suspendisse potenti.</li>
        <li><svg width="14" height="14"><rect width="14" height="14" fill="#eef0ee"/><path d="M5 3 L10 7 L5 11Z" fill="#9aa0a0"/></svg>Etiam enim nisl, i</li>
        <li><svg width="14" height="14"><rect width="14" height="14" fill="#eef0ee"/><path d="M5 3 L10 7 L5 11Z" fill="#9aa0a0"/></svg>Praesent commodo</li>
        <li><svg width="14" height="14"><rect width="14" height="14" fill="#eef0ee"/><path d="M5 3 L10 7 L5 11Z" fill="#9aa0a0"/></svg>Nulla auctor laoreet</li>
      </ul>
      <p class="service-copy">Etiam enim nisl, interdum eu, dictum nec, euismod eu, leo. Morbi dictum. Donec tincidunt. Nam viverra. Donec posuere.</p>
      <a class="service-cta" href="#">click here <b>&gt;&gt;</b></a>
    </article>
  </section>

  <section class="content">
    <div class="news">
      <h2 class="section-title">LATEST NEWS &amp; UPDATES</h2>
      <ul class="news-list">
        <li class="news-item">
          <svg width="26" height="30" viewBox="0 0 26 30"><rect x="1" y="3" width="24" height="26" rx="2" fill="#f2f2f0" stroke="#bfc2c0"/><rect x="1" y="3" width="24" height="7" fill="#c8302c"/><text x="13" y="25" text-anchor="middle" font-family="Arimo, sans-serif" font-weight="700" font-size="15" fill="#6a6e70">7</text></svg>
          <p>Raesent commodo fermentum justo. Mauris posuere. Aliquam semper, orci ac mattis mattis, enim enim dignissim lacus, vel blandit augue massa ut quam. Quisque consequat,</p>
        </li>
        <li class="news-item">
          <svg width="26" height="30" viewBox="0 0 26 30"><rect x="1" y="3" width="24" height="26" rx="2" fill="#f2f2f0" stroke="#bfc2c0"/><rect x="1" y="3" width="24" height="7" fill="#c8302c"/><text x="13" y="25" text-anchor="middle" font-family="Arimo, sans-serif" font-weight="700" font-size="15" fill="#6a6e70">7</text></svg>
          <p>Raesent commodo fermentum justo. Mauris posuere. Aliquam semper, orci ac mattis mattis, enim enim dignissim lacus, vel blandit augue massa ut quam. Quisque consequat,</p>
        </li>
        <li class="news-item">
          <svg width="26" height="30" viewBox="0 0 26 30"><rect x="1" y="3" width="24" height="26" rx="2" fill="#f2f2f0" stroke="#bfc2c0"/><rect x="1" y="3" width="24" height="7" fill="#c8302c"/><text x="13" y="25" text-anchor="middle" font-family="Arimo, sans-serif" font-weight="700" font-size="15" fill="#6a6e70">7</text></svg>
          <p>Raesent commodo fermentum justo. Mauris posuere. Aliquam semper, orci ac mattis mattis, enim enim dignissim lacus, vel blandit augue massa ut quam. Quisque consequat,</p>
        </li>
        <li class="news-item">
          <svg width="26" height="30" viewBox="0 0 26 30"><rect x="1" y="3" width="24" height="26" rx="2" fill="#f2f2f0" stroke="#bfc2c0"/><rect x="1" y="3" width="24" height="7" fill="#c8302c"/><text x="13" y="25" text-anchor="middle" font-family="Arimo, sans-serif" font-weight="700" font-size="15" fill="#6a6e70">7</text></svg>
          <p>Raesent commodo fermentum justo. Mauris posuere. Aliquam semper, orci ac mattis mattis, enim enim dignissim lacus, vel blandit augue massa ut quam. Quisque consequat,</p>
        </li>
      </ul>
    </div>
    <aside class="quick-links">
      <h2 class="section-title">QUICK LINKS</h2>
      <ul>
        <li><a href="#">Suspendisse potenti. Nulla facilisi. Curabitur</a></li>
        <li><a href="#">convallis bibendum felis. In aliquam hen-</a></li>
        <li><a href="#">drerit nisl. Maecenas vulputate. Aenean</a></li>
        <li><a href="#">eget purus vitae felis lacinia semper. Viva-</a></li>
        <li><a href="#">mus nec massa vitae enim aliquam sollici-</a></li>
        <li><a href="#">tudin. Proin lectus diam, egestas eget,</a></li>
        <li><a href="#">placerat id, blandit nec, magna. Nunc nisi</a></li>
        <li><a href="#">arcu, volutpat vitae, vestibulum sit amet,</a></li>
        <li><a href="#">malesuada eget, tortor. Aliquam semper</a></li>
        <li><a href="#">viverra felis. Aliquam rhoncus, felis a</a></li>
        <li><a href="#">tempus eleifend, enim turpis consequat</a></li>
        <li><a href="#">arcu, non fermentum odio elit at lacus. Sed</a></li>
      </ul>
    </aside>
  </section>

  <footer class="site-footer">
    <nav class="footer-links">
      <a href="#">Affiliates</a><span>|</span><a href="#">Customer Login</a><span>|</span><a href="#">Support</a><span>|</span><a href="#">Prices</a>
    </nav>
    <small class="copyright">Copyright 2011</small>
  </footer>

</div>
</body>
</html>
```